App Icon Designs

I am creating an app and I need icons for these categories:
Education
Entertainment
Finance
Games
Health & Fitness
Kids
Lifestyle
Medical
Music
Navigation
News
Photo & Video
Social Networking
Sports
Travel
Utilities
Weather
I would like the icon designs to imitate the style of the included picture. I have also included a picture of the buttons the icons should fit in (75 x 75 pixels). The icons should stick the the simple and flat look.
Please keep all icons 75 x 75 pixels, and NOT 90 x 90 pixels.
Prize increased to $230. Please do your best work. If anyone can successfully imitate the design of the picture included, I will be glad to increase the prize by another $100.

```html
<!DOCTYPE html>
<html lang="en">
<head>
<meta charset="utf-8">
<title>Category Lock Screen</title>
<link rel="stylesheet" href="https://fonts.googleapis.com/css2?family=Open+Sans:wght@400;700&display=swap">
<style>
  :root {
    --page-bg: #eceef2;
    --screen-bg: #eef0f3;
    --bar-dark: #1c1c1c;
    --bar-mid: #3a3a3a;
    --label: #ffffff;
    --business: #5473ad;
    --education: #63bec6;
    --entertainment: #ebbc4b;
    --finance: #1fbb9b;
    --games: #d9628a;
    --icon-case: #d6a33f;
    --icon-cap: #2d6a8c;
    --icon-masks: #c9262f;
    --icon-piggy: #e9c9dc;
    --icon-pad: #6a6a6a;
    --slider-text: #8a8a8a;
  }
  * { box-sizing: border-box; margin: 0; padding: 0; }
  html, body {
    width: 1200px; height: 973px; overflow: hidden;
    background: var(--page-bg);
    font-family: "Open Sans", sans-serif;
  }
  .screen {
    position: absolute; left: 348px; top: 43px;
    width: 504px; height: 888px;
    background: var(--screen-bg);
    overflow: hidden;
  }
  .status-bar {
    height: 32px;
    background: linear-gradient(#444, var(--bar-dark));
    display: flex; align-items: center; justify-content: space-between;
    padding: 0 14px;
  }
  .status-bar svg { display: block; }
  .category-list {
    list-style: none;
    padding: 17px 17px 0;
    display: flex; flex-direction: column; gap: 15px;
  }
  .category {
    position: relative;
    height: 122px; border-radius: 8px;
    display: flex; align-items: center;
    padding-left: 17px;
    overflow: hidden;
  }
  .category::after {
    content: ""; position: absolute; top: 0; right: 0; bottom: 0; width: 45%;
    background: rgba(255,255,255,0.16);
    clip-path: polygon(25% 0, 100% 0, 100% 100%, 55% 100%);
  }
  .category--business { background: var(--business); }
  .category--education { background: var(--education); }
  .category--entertainment { background: var(--entertainment); }
  .category--finance { background: var(--finance); }
  .category--games { background: var(--games); }
  .category-icon {
    width: 91px; height: 76px; border-radius: 10px; flex: none;
  }
  .icon-business { background: var(--icon-case); }
  .icon-education { background: var(--icon-cap); }
  .icon-entertainment { background: var(--icon-masks); }
  .icon-finance { background: var(--icon-piggy); }
  .icon-games { background: var(--icon-pad); }
  .category-label {
    margin-left: 12px;
    color: var(--label);
    font-weight: 700; font-size: 26px;
  }
  .lock-bar {
    position: absolute; left: 0; right: 0; bottom: 0; height: 150px;
    background: linear-gradient(#3b3b3b 0%, #121212 40%, #000 100%);
  }
  .unlock-slider {
    position: absolute; left: 34px; top: 32px;
    width: 431px; height: 78px; border-radius: 12px;
    background: linear-gradient(#0a0a0a, #1d1d1d);
    border: 2px solid #2e2e2e;
    display: flex; align-items: center;
  }
  .unlock-knob {
    width: 106px; height: 70px; margin-left: 2px; border-radius: 10px;
    background: linear-gradient(#fdfdfd, #c9c9c9);
    display: flex; align-items: center; justify-content: center;
  }
  .unlock-text {
    margin-left: 30px;
    color: var(--slider-text);
    font-size: 36px; font-weight: 400;
  }
</style>
</head>
<body>
  <main class="screen">
    <header class="status-bar">
      <svg width="30" height="14" viewBox="0 0 30 14" aria-label="Signal">
        <rect x="0" y="10" width="4" height="4" fill="#fff"/>
        <rect x="6" y="8" width="4" height="6" fill="#fff"/>
        <rect x="12" y="6" width="4" height="8" fill="#fff"/>
        <rect x="18" y="3" width="4" height="11" fill="#fff"/>
        <rect x="24" y="0" width="4" height="14" fill="#fff"/>
      </svg>
      <svg width="16" height="20" viewBox="0 0 16 20" aria-label="Locked">
        <path d="M4 9V6a4 4 0 0 1 8 0v3" fill="none" stroke="#fff" stroke-width="2.4"/>
        <rect x="1" y="9" width="14" height="11" rx="2" fill="#fff"/>
      </svg>
      <svg width="32" height="16" viewBox="0 0 32 16" aria-label="Battery">
        <rect x="1" y="1" width="27" height="14" rx="2" fill="none" stroke="#fff" stroke-width="2"/>
        <rect x="4" y="4" width="21" height="8" fill="#fff"/>
        <rect x="29" y="5" width="3" height="6" fill="#fff"/>
      </svg>
    </header>

    <ul class="category-list">
      <li class="category category--business">
        <div class="category-icon icon-business" role="img" aria-label="Flat briefcase icon"></div>
        <span class="category-label">Business</span>
      </li>
      <li class="category category--education">
        <div class="category-icon icon-education" role="img" aria-label="Flat graduation cap icon"></div>
        <span class="category-label">Education</span>
      </li>
      <li class="category category--entertainment">
        <div class="category-icon icon-entertainment" role="img" aria-label="Flat theatre masks icon"></div>
        <span class="category-label">Entertainment</span>
      </li>
      <li class="category category--finance">
        <div class="category-icon icon-finance" role="img" aria-label="Flat piggy bank with coin icon"></div>
        <span class="category-label">Finance</span>
      </li>
      <li class="category category--games">
        <div class="category-icon icon-games" role="img" aria-label="Flat game controller buttons icon"></div>
        <span class="category-label">Games</span>
      </li>
    </ul>

    <footer class="lock-bar">
      <div class="unlock-slider">
        <div class="unlock-knob">
          <svg width="48" height="30" viewBox="0 0 48 30" aria-label="Arrow">
            <path d="M2 10h26V2l18 13-18 13v-8H2z" fill="#7d7d7d"/>
          </svg>
        </div>
        <span class="unlock-text">slide to unlock</span>
      </div>
    </footer>
  </main>
</body>
</html>
```